Vessa Almond Protein - Less, but better

Design a protein powder pouch (350g). Take inspiration from Brimora.co and put the same information on the pouch and add "made in Australia". I do not want it to be exactly the same design but just take some inspiration from it.

```html
<!DOCTYPE html>
<html lang="en">
<head>
<meta charset="utf-8">
<title>Vessa Almond Protein Powder – Pouch</title>
<link rel="stylesheet" href="https://fonts.googleapis.com/css2?family=Jost:wght@400;500&family=Roboto:wght@400;500;700&display=swap">
<style>
  :root {
    --page: #ffffff;
    --pouch-cream: #efeee6;
    --blush: #d8aeaa;
    --sage: #6e9688;
    --ink: #26261f;
    --mustard: #e2b033;
    --vanilla-text: #fbf4e2;
    --small-ink: #3a3a34;
  }
  * { box-sizing: border-box; margin: 0; padding: 0; }
  html, body { width: 1200px; height: 900px; overflow: hidden; background: var(--page); }
  .canvas { position: relative; width: 1200px; height: 900px; }

  .pouch {
    position: absolute; left: 370px; top: 95px;
    width: 460px; height: 680px;
    border-radius: 28px 28px 6px 6px;
    background: var(--pouch-cream);
    overflow: hidden;
  }
  .pouch-art { position: absolute; inset: 0; width: 460px; height: 680px; }

  .brand-name {
    position: absolute; left: 40px; top: 190px;
    font-family: "Jost", sans-serif; font-weight: 500;
    font-size: 40px; line-height: 1; letter-spacing: 1px;
    color: var(--ink); white-space: nowrap;
  }
  .tagline {
    position: absolute; left: 42px; top: 240px;
    font-family: "Jost", sans-serif; font-weight: 400;
    font-size: 16px; color: var(--sage); white-space: nowrap; letter-spacing: 0.5px;
  }

  .product-title {
    position: absolute; left: 227px; top: 270px;
    font-family: "Jost", sans-serif; font-weight: 400;
    font-size: 35px; line-height: 1.0; color: var(--ink); letter-spacing: 0.3px;
  }
  .flavour-band {
    position: absolute; left: 222px; top: 384px;
    width: 178px; height: 34px;
    background: var(--mustard);
    border-radius: 0 10px 0 0;
    font-family: "Roboto", sans-serif; font-weight: 500;
    font-size: 15px; letter-spacing: 1.4px; color: var(--vanilla-text);
    line-height: 34px; padding-left: 12px;
  }
  .claims {
    position: absolute; left: 224px; top: 430px;
    font-family: "Roboto", sans-serif; font-size: 9.5px; color: var(--small-ink);
    letter-spacing: 0.2px; white-space: nowrap;
  }
  .claims-rule {
    position: absolute; left: 224px; top: 446px; width: 108px;
    border-top: 1.5px dotted var(--small-ink);
  }
  .health {
    position: absolute; left: 224px; top: 457px;
    font-family: "Roboto", sans-serif; font-size: 9.5px; line-height: 1.3;
    color: var(--small-ink); letter-spacing: 0.2px;
  }
  .origin {
    position: absolute; left: 224px; top: 520px;
    font-family: "Roboto", sans-serif; font-size: 8.5px; letter-spacing: 1.2px;
    color: var(--sage);
  }
  .protein-badge {
    position: absolute; left: 334px; top: 527px;
    width: 74px; height: 74px; border-radius: 50%;
    background: var(--pouch-cream); border: 2px solid var(--sage);
    display: flex; flex-direction: column; align-items: center; justify-content: center;
    font-family: "Roboto", sans-serif; color: var(--ink); text-align: center;
  }
  .protein-amount { font-weight: 700; font-size: 22px; line-height: 1; }
  .protein-label { font-weight: 700; font-size: 7.5px; line-height: 1.05; margin-top: 2px; }
</style>
</head>
<body>
<main class="canvas">
  <section class="pouch" aria-label="Vessa Almond Protein Powder pouch, front">
    <svg class="pouch-art" viewBox="0 0 460 680" aria-hidden="true">
      <path fill="var(--blush)" d="M92 0 C130 40 140 105 185 145 C225 180 265 200 300 225 C340 255 400 268 460 272 L460 0 Z"/>
      <path fill="var(--sage)" d="M0 680 L0 662 C60 640 150 622 240 622 C330 622 385 592 460 570 L460 680 Z"/>
    </svg>

    <div class="brand-name">Vessa</div>
    <div class="tagline">less, but better</div>

    <h1 class="product-title">ALMOND<br>PROTEIN<br>POWDER</h1>
    <div class="flavour-band">REAL VANILLA</div>

    <p class="claims">VEGAN | JUST 4 INGREDIENTS | DELICIOUS</p>
    <div class="claims-rule"></div>
    <p class="health">SUPPORTS HEALTH:<br>HEART, DIGESTION, INMUNE<br>SYSTEM, SKIN, BONE, HAIR</p>
    <p class="origin">MADE IN AUSTRALIA</p>

    <div class="protein-badge">
      <span class="protein-amount">18g</span>
      <span class="protein-label">PLANT<br>PROTEIN</span>
    </div>
  </section>
</main>
</body>
</html>
```